Brivane Communications - veteran and exclusive boutique copywriting agency

PROJECT NEEDS:
1. Website design - full homepage design and inner page top banner design
2. Logo design
* Please see attached Briefs (Word Docs) for descriptions of what is needed for 1 and 2 above.
ABOUT THE CLIENT:
Brivane Communications is a veteran and exclusive boutique copywriting agency run by Martin Olafsky. Martin is an award-winning published novelist and an accomplished executive ghostwriter with articles regularly published prominent technology publications like Pulsar, ByteHarbor, CapitalDrift, and more. For nearly three decades, Martin has focused solely on the technology sector - serving clients in Israel, Europe and the US.

Target Market(s)

hi-tech companies run by serious, confident professionals.

Industry/Entity Type

Business

Number of Pages Required

2 page

Font styles to use
Sans Serif
Other font styles liked:
• font should be modern

Colors
0054AA
0677BA
7BADD7
CADEEF
E8F1F8
F0912C
F2A743
F7CA91
FBE8D2
FDF5EE

Requirements
Must have
• psd files for logo, homepage design, and inner page top banner design
Nice to have
• Please see attached Website and Logo Design Briefs (Word Docs)
Should not have

```html
<!DOCTYPE html>
<html lang="en">
<head>
<meta charset="utf-8">
<title>Brivane Communications</title>
<link href="https://fonts.googleapis.com/css2?family=Bebas+Neue&family=Montserrat:ital,wght@0,400;0,500;0,600;0,700;0,800;1,500;1,600;1,700&display=swap" rel="stylesheet">
<style>
:root{
  --orange:#F5A623;
  --orange-deep:#F0912C;
  --navy:#243A6A;
  --navy-dark:#1C2E55;
  --steel:#6283A8;
  --card:#6B8CB2;
  --ink:#2B2B2B;
  --body:#4A4A4A;
  --gray-band:#ECECEC;
  --pale-circle:#F1F1F1;
  --cream:#F8E5BE;
  --white:#FFFFFF;
}
*{margin:0;padding:0;box-sizing:border-box}
html,body{width:1200px;height:5254px;overflow:hidden;background:var(--white)}
body{font-family:"Montserrat",sans-serif;color:var(--body)}
.page{position:relative;width:1200px;height:5254px;overflow:hidden}
.backdrop{position:absolute;left:0;top:0}
.abs{position:absolute}
.photo{position:absolute}
.btn{position:absolute;display:inline-block;background:var(--orange);color:var(--white);font-size:13px;font-weight:500;border-radius:16px;text-align:center;height:30px;line-height:30px}

/* header */
.brand{left:163px;top:14px;width:200px;font-weight:800;color:var(--navy);font-size:30px;line-height:30px;letter-spacing:1px}
.brand small{display:block;font-size:14px;letter-spacing:3.4px;line-height:22px}
.nav{left:510px;top:36px;display:flex;gap:24px;font-size:13px;font-weight:500;color:#3a3a3a;text-transform:uppercase}
.nav .active{color:var(--orange)}
.nav-contact{left:938px;top:31px;width:100px}

/* hero */
.hero-title{left:163px;top:170px;font-family:"Bebas Neue",sans-serif;font-size:98px;line-height:84px;color:var(--orange);letter-spacing:1px}
.hero-sub{left:163px;top:340px;width:360px;font-size:14px;line-height:24px;color:#333}
.hero-btn{left:161px;top:412px;width:100px}

/* clients */
.clients{left:160px;top:838px;width:880px;display:flex;justify-content:space-between;align-items:center}
.client{display:flex;align-items:center;gap:8px;font-weight:700;font-size:18px;color:#5D6E86}
.client i{display:inline-block;width:14px;height:14px;border-radius:50%;background:#9FB3CB}
.arrow-btn{position:absolute;width:26px;height:26px;border:1.5px solid #777;border-radius:50%}

/* headings */
.h2{font-size:36px;font-weight:500;color:var(--ink);line-height:42px}
.kicker{color:var(--orange);font-size:21px;font-weight:600}
.lead-i{color:var(--orange);font-style:italic;font-size:13px;font-weight:600;line-height:24px}
.copy{font-size:13.5px;line-height:24px;color:#444}
.copy p+p{margin-top:24px}

/* services */
.service{position:absolute;top:1652px;width:270px;height:245px;background:var(--card);border-radius:4px;color:var(--white);text-align:center;padding-top:82px}
.service h3{font-size:18px;font-weight:500;color:var(--orange);margin-bottom:6px}
.service h4{font-size:13px;font-weight:600;margin-bottom:10px}
.service p{font-size:13px;line-height:24px;padding:0 10px}
.service-icon{position:absolute;top:-70px;left:63px;width:140px;height:140px;border-radius:50%;background:var(--orange);border:7px solid var(--white);box-shadow:0 4px 10px rgba(0,0,0,.15)}

/* why choose */
.reason{position:absolute;left:163px;display:flex;gap:24px;width:380px}
.reason-icon{flex:none;width:62px;height:62px;border-radius:8px;background:#F3E3C4}
.reason p{font-size:13px;line-height:24px;color:#333}
.reason b{font-weight:700}

/* testimonial */
.testimonial{left:0;top:2890px;width:1200px;text-align:center;color:var(--white)}
.testimonial h2{font-size:36px;font-weight:500;margin-bottom:18px}
.testimonial blockquote{font-style:italic;font-size:16px;line-height:30px;width:720px;margin:0 auto}
.testimonial cite{display:block;margin-top:30px;font-style:normal;font-weight:700;font-size:12px}

/* footer */
.foot-h{font-size:14px;font-weight:600;color:var(--white)}
.foot-links{font-size:12px;line-height:30px;color:var(--white)}
.foot-links .current{text-decoration:underline;text-decoration-color:var(--orange)}
.contact-line{position:absolute;left:522px;display:flex;gap:12px;font-size:12px;line-height:22px;color:var(--white)}
.contact-line svg{flex:none;margin-top:3px}
.foot-brand{left:785px;top:5030px;width:260px;text-align:center;color:var(--white)}
.foot-brand strong{display:block;font-size:34px;font-weight:800;letter-spacing:2px;line-height:44px}
.foot-brand span{display:block;font-size:13px;font-weight:500;letter-spacing:.5px}
.socials{left:864px;top:5152px;display:flex;gap:8px}
.socials i{width:24px;height:24px;border-radius:50%;background:#2F7FD3;border:2px solid var(--white)}
.copyright{left:0;top:5202px;width:1200px;height:52px;background:var(--navy-dark);color:var(--white);font-size:11px;text-align:center;line-height:52px}
</style>
</head>
<body>
<div class="page">

<svg class="backdrop" width="1200" height="5254" viewBox="0 0 1200 5254" aria-hidden="true">
  <!-- hero decoration -->
  <circle cx="60" cy="80" r="175" fill="none" stroke="#ECEEF2" stroke-width="30"/>
  <circle cx="898" cy="377" r="153" fill="var(--orange)"/>
  <path d="M0 540 C150 520 300 560 450 600 C600 640 800 640 980 575 L1010 600 C800 670 600 665 450 632 C300 600 150 578 0 602 Z" fill="var(--orange)"/>
  <path d="M0 590 C200 565 400 640 620 655 C850 670 1000 600 1200 555 L1200 615 C1000 650 850 712 620 706 C400 700 200 655 0 642 Z" fill="var(--navy)"/>

  <!-- what i do band -->
  <path d="M0 1500 C300 1470 600 1540 850 1500 C1000 1475 1100 1445 1200 1440 L1200 1850 L0 1870 Z" fill="var(--gray-band)"/>
  <path d="M930 1470 C1030 1460 1120 1430 1200 1420 L1200 1455 C1110 1465 1030 1480 930 1470 Z" fill="var(--navy)"/>
  <path d="M0 1850 C300 1880 500 1960 750 1900 C950 1855 1100 1830 1200 1830 L1200 1870 C1050 1880 950 1920 750 1965 C500 2015 250 1992 0 1992 Z" fill="var(--orange)"/>

  <!-- why choose me circles -->
  <circle cx="847" cy="2387" r="306" fill="var(--pale-circle)"/>
  <circle cx="816" cy="2428" r="180" fill="var(--cream)"/>

  <!-- testimonial band -->
  <path d="M0 3150 C200 3130 400 3230 600 3250 C800 3270 1000 3200 1200 3170 L1200 3240 C1000 3290 800 3322 600 3306 C400 3290 200 3222 0 3222 Z" fill="var(--orange)"/>
  <path d="M0 2760 C200 2840 400 2800 650 2770 C850 2750 1050 2760 1200 2770 L1200 2830 L0 2880 Z" fill="var(--navy)"/>
  <path d="M0 2852 C200 2880 400 2832 650 2802 C850 2782 1050 2792 1200 2802 L1200 3200 C1000 3240 800 3290 600 3260 C400 3232 200 3150 0 3172 Z" fill="var(--steel)"/>
  <circle cx="1132" cy="2806" r="78" fill="none" stroke="#A9B9CF" stroke-width="26"/>
  <circle cx="1132" cy="2806" r="40" fill="#4F6E95"/>
  <path d="M70 3200 A130 130 0 0 1 330 3200" fill="none" stroke="#8BA2C0" stroke-width="28"/>

  <!-- author band -->
  <path d="M0 4130 C300 4080 700 4090 1000 4110 C1100 4116 1160 4110 1200 4100 L1200 4900 L0 4900 Z" fill="var(--gray-band)"/>
  <path d="M1040 4100 C1100 4102 1160 4090 1200 4075 L1200 4110 C1150 4125 1100 4125 1040 4100 Z" fill="var(--navy)"/>

  <!-- footer waves -->
  <path d="M0 4818 C250 4870 500 4900 750 4880 C950 4860 1100 4830 1200 4810 L1200 4870 C1000 4910 750 4950 500 4945 C300 4940 150 4900 0 4880 Z" fill="var(--orange)"/>
  <path d="M0 4860 C200 4910 450 4935 700 4925 C900 4915 1080 4880 1200 4850 L1200 5210 L0 5210 Z" fill="var(--navy)"/>
  <line x1="453" y1="5000" x2="453" y2="5180" stroke="#3E5283" stroke-width="1"/>
  <line x1="755" y1="5000" x2="755" y2="5180" stroke="#3E5283" stroke-width="1"/>
</svg>

<!-- header -->
<div class="abs brand">BRIVANE<small>COMMUNICATIONS</small></div>
<nav class="abs nav"><span class="active">Home</span><span>About</span><span>Industries</span><span>Portfolio</span><span>Clients</span></nav>
<span class="btn nav-contact">Contact</span>

<!-- hero -->
<h1 class="abs hero-title">Your voice,<br>my words.</h1>
<p class="abs hero-sub">Copywriting and executive ghostwriting that speaks for your vision and your technology.</p>
<span class="btn hero-btn">Contact</span>
<div class="photo" role="img" aria-label="Portrait of Martin Olafsky in a light blue shirt and jeans" style="left:755px;top:110px;width:290px;height:440px;border-radius:140px 140px 20px 20px;background:linear-gradient(180deg,#D9C2AE 0%,#A8BFDD 35%,#8FAAD0 70%,#4C6C9C 100%)"></div>

<!-- clients -->
<span class="arrow-btn" style="left:97px;top:843px"></span>
<span class="arrow-btn" style="left:1070px;top:843px"></span>
<div class="abs clients">
  <span class="client">Kestrel</span>
  <span class="client"><i></i>Valmont</span>
  <span class="client">Teravolt</span>
  <span class="client"><i></i>Genaris</span>
  <span class="client">Clinora</span>
  <span class="client">Medovra</span>
</div>

<!-- what i do -->
<div class="abs" style="left:161px;top:1035px;width:410px;height:478px;background:var(--white);border-radius:70px 0 80px 0;box-shadow:0 6px 20px rgba(0,0,0,.12)"></div>
<div class="photo" role="img" aria-label="Martin Olafsky seated in a dark sweater" style="left:178px;top:1048px;width:378px;height:452px;border-radius:60px 0 70px 0;background:linear-gradient(160deg,#3A3A3A 0%,#1E1E1E 55%,#3C4C66 100%)"></div>
<h2 class="abs h2" style="left:624px;top:1032px">What I do</h2>
<div class="abs kicker" style="left:624px;top:1083px">The Art Of Business Communication</div>
<div class="abs copy" style="left:624px;top:1125px;width:420px">
  <p>Lorem ipsum dolor sit amet, consectetuer adipiscing elit, sed diam nonummy nibh euismod tincidunt ut laoreet dolore magna aliquam erat volutpat. Ut wisi enim ad minim veniam, corper suscipit lobortis nisl ut aliquip ex ea commodo consequat.</p>
  <p>Duis autem vel eum iriure dolor in hendrerit in vulputate velit esse molestie consequat, vel illum dolore eu feugiat nulla facilisis .</p>
</div>

<!-- services -->
<div class="service" style="left:161px"><span class="service-icon" role="img" aria-label="Speech bubbles icon"></span><h3>Messaging</h3><h4>The Value of a Fresh Perspective</h4><p>Could you be reaching farther? Clearly-defined, accurately-targeted messaging is crucial.</p></div>
<div class="service" style="left:465px"><span class="service-icon" role="img" aria-label="Document with approval tick icon"></span><h3>Collateral</h3><h4>Concise, Effective, Creative</h4><p>Marketing collateral that effectively communicates who you are and what you want to say.</p></div>
<div class="service" style="left:768px"><span class="service-icon" role="img" aria-label="Document with paper plane icon"></span><h3>Content Marketing</h3><h4>Giving Voice to Your Vision</h4><p>Articles, blog content, white papers, e-books. Your ideas and expertise, our words.</p></div>

<!-- why choose me -->
<h2 class="abs h2" style="left:161px;top:2078px">Why Choose Me</h2>
<p class="abs lead-i" style="left:163px;top:2130px;width:440px">In nearly two decades in the international marketing trenches, I've learned to rapidly define and internalize company messages - and to communicate them at eye-level.</p>
<div class="reason" style="top:2246px"><span class="reason-icon" role="img" aria-label="Two people icon"></span><p>I do all client writing myself, so my clients get <b>one-on-one service</b> and a <b>personal guarantee of quality.</b></p></div>
<div class="reason" style="top:2366px"><span class="reason-icon" role="img" aria-label="Shirt and tie icon"></span><p>My writing is <b>concise, elegant, and professional</b> - while at the same time reflecting an understated creativity and sense of humor that brings company messages to a very intimate, personal level.</p></div>
<div class="reason" style="top:2532px"><span class="reason-icon" role="img" aria-label="Connected network cloud icon"></span><p>I offer clients a <b>deep understanding of business, communication, and technology</b> - coupled with a hard-hitting and concise, yet elegant writing style.</p></div>
<span class="btn" style="left:245px;top:2662px;width:100px">Contact</span>
<div class="photo" role="img" aria-label="Martin Olafsky smiling in a grey sweater and jeans" style="left:640px;top:2045px;width:360px;height:695px;border-radius:150px 150px 0 0;background:linear-gradient(180deg,#D7B9A2 0%,#6D6E70 28%,#58595B 60%,#5A7AA6 100%)"></div>

<!-- testimonial -->
<div class="abs testimonial">
  <h2>What They’re Saying</h2>
  <blockquote>Martin is a terrific resource for our company. A self-starter, who has generated a great deal of revenue for us and does high-quality work. Highly recommended.</blockquote>
  <cite>Dov Reshef, CEO, Harborline Security</cite>
</div>
<span class="arrow-btn" style="left:162px;top:2979px;border-color:#fff"></span>
<span class="arrow-btn" style="left:1012px;top:2979px;border-color:#fff"></span>

<!-- about -->
<div class="abs" style="left:163px;top:3448px;width:410px;height:552px;background:var(--white);border-radius:70px 0 80px 0;box-shadow:0 6px 20px rgba(0,0,0,.12)"></div>
<div class="photo" role="img" aria-label="Martin Olafsky standing with arms crossed in a white sweater" style="left:180px;top:3460px;width:378px;height:528px;border-radius:60px 0 70px 0;background:linear-gradient(180deg,#B7AEA5 0%,#D9D2CA 50%,#C9BFB4 100%)"></div>
<h2 class="abs h2" style="left:608px;top:3510px;width:420px">About Martin Olafsky</h2>
<p class="abs lead-i" style="left:608px;top:3594px;width:432px">In nearly two decades in the international marketing trenches, I've learned to rapidly define and internalize company messages - and to communicate them at eye-level.</p>
<div class="abs copy" style="left:608px;top:3676px;width:432px">
  <p>Born and raised in the US, I've lived and worked in Israel since 1990, and speak fluent Hebrew. I do all client writing myself, so my clients get one-on-one service and a personal guarantee of quality.</p>
  <p>My writing is concise, elegant, and professional - while at the same time reflecting an understated creativity and sense of humor that brings company messages to a very intimate, personal level. I offer clients a deep understanding of business, communication, and technology - coupled with a hard-hitting and concise, yet elegant writing style.</p>
</div>

<!-- author -->
<h2 class="abs h2" style="left:161px;top:4212px;width:420px">Martin’s Work<br>As An Author</h2>
<p class="abs lead-i" style="left:163px;top:4288px;color:var(--navy);font-weight:700">Writer, Dad, Musician, Gardener...<br>Not Necessarily in that Order</p>
<div class="abs copy" style="left:163px;top:4356px;width:440px">
  <p>I was born in 1967 near Millbrook, Texas, and grew up uneventfully in Harlan Springs, Ohio - birthplace of Dana Whitfield and fictional home of the Field Unit 9 character Major Hollis, among others. When you grow up in a place like Harlan Springs, any claim to fame is important...</p>
  <p>After completing my BA at Midland State University - during the course of which I also studied at Northgate University and Coastal Bay University - I emigrated to Israel only months before the first Gulf War, in August 1990. In between planeloads of immigrants from the former Soviet Union, I was given an Israeli ID card and a gas mask, in that order. I'm still not sure which one these ultimately produced greater headaches.</p>
</div>
<span class="btn" style="left:161px;top:4716px;width:116px">Read More</span>
<div class="abs" style="left:622px;top:4121px;width:420px;height:714px;background:var(--white);border-radius:70px 0 80px 0;box-shadow:0 6px 20px rgba(0,0,0,.12)"></div>
<div class="photo" role="img" aria-label="Martin Olafsky in a white shirt" style="left:640px;top:4133px;width:385px;height:560px;border-radius:60px 0 0 0;background:linear-gradient(180deg,#6E6A66 0%,#9A948D 40%,#E4E2DF 100%)"></div>
<div class="photo" role="img" aria-label="Three of Martin Olafsky's novels standing side by side" style="left:620px;top:4600px;width:450px;height:230px;border-radius:4px;background:linear-gradient(90deg,#2E2B2A 0%,#5A4A3A 33%,#B9A58C 50%,#C98A4A 75%,#7A4A2A 100%)"></div>

<!-- footer -->
<div class="abs foot-h" style="left:161px;top:5006px">Quick Links</div>
<div class="abs foot-links" style="left:161px;top:5048px"><span class="current">Home</span><br>About<br>Services<br>Industries</div>
<div class="abs foot-links" style="left:263px;top:5048px">Portfolio<br>Clients<br>Contact</div>
<div class="abs foot-h" style="left:522px;top:5006px">Contact Us</div>
<div class="contact-line" style="top:5050px"><svg width="14" height="16" viewBox="0 0 14 16"><path d="M7 1a5 5 0 0 0-5 5c0 4 5 9 5 9s5-5 5-9a5 5 0 0 0-5-5z" fill="none" stroke="#F5A623" stroke-width="1.6"/><circle cx="7" cy="6" r="1.8" fill="#F5A623"/></svg><span>P.O. Box 4821<br>Nirot, Israel 40519</span></div>
<div class="contact-line" style="top:5116px"><svg width="14" height="16" viewBox="0 0 14 16"><rect x="1" y="3" width="12" height="9" fill="none" stroke="#F5A623" stroke-width="1.6"/><path d="M1 3l6 5 6-5" fill="none" stroke="#F5A623" stroke-width="1.6"/></svg><span>hello@brivane.example</span></div>
<div class="contact-line" style="top:5154px;font-weight:600;font-size:13px"><svg width="14" height="16" viewBox="0 0 14 16"><rect x="3" y="1" width="8" height="14" rx="1.5" fill="none" stroke="#F5A623" stroke-width="1.6"/></svg><span>+972-54-210-8876</span></div>
<div class="abs foot-brand"><strong>BRIVANE</strong><span>THE ART OF BUSINESS COMMUNICATION</span></div>
<div class="abs socials"><i></i><i></i><i></i></div>
<div class="abs copyright">© 2023 Brivane The Art of Business Communication. All Right Reserved.</div>

</div>
</body>
</html>
```